Rodent & Wildlife Services from Harborline Termite & Pest Control

I want to show all of the steps in our Rodent/Wildlife Treatment plan:
Inspection- a Harborline wildlife specialist will do a thorough inspection of the Attic and exterior of your home. We will provide you will a detailed Report and Pictures of any infestations found and any areas found to be contaminated. We will also identify any current or potential entry points into the home.
Trapping/Removal- we will create a plan to trap any infestation and remove them- each situation is different and may require a variety of techniques.
Decontamination- animals will leave behind urine, feces, and oils that can potentially contain a variety of bacterias and deseases. We will include in the treatment plan a process to remove and clean up these areas.
Entry Prevention- it is very important to seal up any potential entry points after the infestation has been eliminated. This will help prevent any future infestations into the structure.
Ongoing Protection- Harborline will set up a Rodent baiting program to reduce any surrounding populations.

my thought is to have a picture of each Step and then description (bullet points) about that step

Target Market(s)

Residential

Industry/Entity Type

Pest Control

Font styles to use
Other font styles liked:
• Times Roman

Colors
0455a3
ec1f27

Requirements
Must have
• Professional, concise look.

```html
<!DOCTYPE html>
<html lang="en">
<head>
<meta charset="utf-8">
<title>Harborline Termite &amp; Pest Control – Rodent &amp; Wildlife Services</title>
<link href="https://fonts.googleapis.com/css2?family=Bebas+Neue&family=Roboto+Condensed:wght@300;400;700&display=swap" rel="stylesheet">
<style>
  :root{
    --brand-blue:#0455a3;
    --panel-blue:#1b63c0;
    --panel-blue-dark:#0b4fa6;
    --brand-red:#ec1f27;
    --footer-red:#c8161d;
    --accent-gold:#f5c342;
    --light-bg:#f2f2f2;
    --text-dark:#222222;
    --icon-grey:#7d7d7d;
    --stage:#e4e4e4;
    --white:#ffffff;
  }
  *{box-sizing:border-box;margin:0;padding:0}
  html,body{width:946px;height:1200px;overflow:hidden}
  body{background:var(--stage);font-family:"Roboto Condensed",Arial,sans-serif;color:var(--text-dark)}
  .flyer{position:absolute;left:49px;top:0;width:848px;height:1200px;background:var(--light-bg);overflow:hidden}

  .hero{position:absolute;left:0;top:0;width:848px;height:262px}
  .hero-title{position:absolute;right:32px;top:22px;text-align:right;font-family:"Bebas Neue",Impact,sans-serif;font-weight:400;color:var(--white);font-size:62px;line-height:56px;letter-spacing:1px;text-shadow:0 2px 4px rgba(0,0,0,.35)}
  .service-area{position:absolute;left:303px;top:142px;width:545px;height:86px;background:rgba(28,72,30,.8);border-radius:14px 0 0 14px;padding:9px 32px 0 20px;text-align:right;color:var(--white);font-size:17px;line-height:22.5px}
  .wave{position:absolute;left:0;top:180px}

  .side-column{position:absolute;left:26px;top:300px;width:250px}
  .side-icon{display:block;margin:0 auto 10px}
  .side-heading{font-weight:700;color:var(--brand-red);font-size:17px;line-height:21px;margin-bottom:8px}
  .side-list{list-style:none}
  .side-list li{position:relative;padding-left:16px;font-size:13.3px;line-height:20px;margin-bottom:5px;font-weight:300}
  .side-list li::before{content:"";position:absolute;left:0;top:5px;width:10px;height:10px;border-radius:50%;border:3px solid var(--brand-blue)}
  .side-list .term{color:var(--brand-red);font-weight:400}
  .side-section{margin-bottom:22px}

  .panel{position:absolute;left:292px;top:258px;width:556px;height:880px;background:linear-gradient(180deg,var(--panel-blue) 0%,var(--panel-blue-dark) 100%)}
  .col{position:absolute;color:var(--white);font-size:13.3px;font-weight:300}
  .col-mid{left:8px;top:88px;width:256px}
  .col-right{left:280px;top:132px;width:256px}
  .block-heading{display:flex;align-items:flex-end;gap:12px;font-weight:700;color:var(--accent-gold);font-size:19px;letter-spacing:.5px;margin-bottom:10px;line-height:22px}
  .panel-list{list-style:none}
  .panel-list>li{position:relative;padding-left:18px;line-height:20px;margin-bottom:4px}
  .panel-list>li::before{content:"";position:absolute;left:0;top:5px;width:10px;height:10px;border-radius:50%;background:var(--brand-red) radial-gradient(circle at 55% 50%,var(--white) 0 2px,transparent 2.5px)}
  .panel-list .sub{padding-left:18px}
  .panel-list .sub::before{display:none}
  .panel-list .term{color:var(--accent-gold);font-weight:400}
  .col-right .panel-list>li{line-height:22px;margin-bottom:6px}
  .mid-block{margin-bottom:22px}

  .badge-award{position:absolute;left:300px;top:12px}
  .badge-offer{position:absolute;left:424px;top:7px;width:104px;height:103px;border-radius:7px;background:linear-gradient(180deg,#ef3b3f,#c1151b);border:2px solid #e6e6e6;color:var(--white);text-align:center;font-weight:700}
  .badge-offer .buy{font-size:9px;letter-spacing:1px;margin-top:4px;opacity:.9}
  .badge-offer .deal{font-size:9.5px;line-height:11px;margin-top:2px}

  .footer-band{position:absolute;left:0;top:1132px;width:848px;height:46px;background:var(--footer-red)}
  .footer-base{position:absolute;left:0;top:1178px;width:848px;height:22px;background:var(--brand-blue)}
  .site-url{position:absolute;left:303px;top:1140px;color:var(--white);font-size:23px;letter-spacing:2.5px}
  .follow{position:absolute;left:614px;top:1147px;display:flex;align-items:center;gap:5px;color:var(--white);font-size:14px}
  .follow .social-slot{width:18px;height:18px;border:1.5px solid var(--white);border-radius:2px}
  .follow span{margin-right:6px}

  .brand-box{position:absolute;left:26px;top:1042px;width:252px;height:158px;background:var(--white);display:flex;flex-direction:column;align-items:center;justify-content:center;gap:8px}
  .brand-name{font-weight:700;color:var(--brand-red);text-align:center;line-height:1}
  .brand-name .main{display:block;font-size:42px}
  .brand-name .sub{display:block;font-size:18px;letter-spacing:1px;margin-top:6px}
  .brand-mark{width:16px;height:16px;background:var(--brand-blue)}
</style>
</head>
<body>
<div class="flyer">

  <svg class="hero" width="848" height="262" viewBox="0 0 848 262" role="img" aria-label="Photograph of a grey mouse standing on green grass under a bright blue sky">
    <defs>
      <linearGradient id="heroFill" x1="0" y1="0" x2="1" y2="1">
        <stop offset="0" stop-color="#f6f7f8"/>
        <stop offset="0.35" stop-color="#b9cfee"/>
        <stop offset="0.6" stop-color="#4a86d6"/>
        <stop offset="0.85" stop-color="#6ea244"/>
        <stop offset="1" stop-color="#3f7a24"/>
      </linearGradient>
    </defs>
    <rect width="848" height="262" fill="url(#heroFill)"/>
  </svg>

  <h1 class="hero-title">QUALITY CARE<br>PEST FREE LIVING</h1>
  <p class="service-area">Providing Pest, Rodent, Wildlife and Termite Control Services in Austin, Houston, San Antonio, and all of the Dallas / Fort Worth Metroplex including Arlington, Frisco, Irving, and Plano.</p>

  <svg class="wave" width="848" height="120" viewBox="0 0 848 120" aria-hidden="true">
    <path d="M0 52 C120 120 300 95 470 70 C620 48 760 50 848 52 L848 120 L0 120 Z" fill="var(--light-bg)"/>
    <path d="M0 40 C110 115 300 90 470 64 C620 42 760 44 848 46 L848 60 C760 58 620 60 470 78 C300 100 110 120 0 60 Z" fill="var(--brand-blue)"/>
  </svg>

  <section class="side-column">
    <div class="side-section">
      <svg class="side-icon" width="62" height="58" viewBox="0 0 62 58" aria-hidden="true">
        <g fill="var(--icon-grey)">
          <circle cx="22" cy="22" r="14"/>
          <g transform="translate(22 22)"><rect x="-4" y="-21" width="8" height="42"/><rect x="-21" y="-4" width="42" height="8"/><rect x="-4" y="-21" width="8" height="42" transform="rotate(45)"/><rect x="-4" y="-21" width="8" height="42" transform="rotate(-45)"/></g>
          <circle cx="46" cy="42" r="8"/>
          <g transform="translate(46 42)"><rect x="-2.5" y="-12" width="5" height="24"/><rect x="-12" y="-2.5" width="24" height="5"/><rect x="-2.5" y="-12" width="5" height="24" transform="rotate(45)"/><rect x="-2.5" y="-12" width="5" height="24" transform="rotate(-45)"/></g>
        </g>
        <circle cx="22" cy="22" r="6" fill="var(--light-bg)"/>
        <circle cx="46" cy="42" r="3.5" fill="var(--light-bg)"/>
      </svg>
      <h2 class="side-heading">OUR RODENT &amp; WILDLIFE PLAN</h2>
      <ul class="side-list">
        <li>Inspection; Trapping/Removal; Decontamination; Entry Prevention; Ongoing Protection</li>
      </ul>
    </div>

    <div class="side-section">
      <svg class="side-icon" width="56" height="58" viewBox="0 0 56 58" aria-hidden="true">
        <circle cx="22" cy="22" r="17" fill="none" stroke="var(--icon-grey)" stroke-width="4"/>
        <path d="M13 22 L20 29 L32 15" fill="none" stroke="var(--icon-grey)" stroke-width="4"/>
        <path d="M35 35 L52 54" stroke="var(--icon-grey)" stroke-width="7" stroke-linecap="round"/>
      </svg>
      <h2 class="side-heading">STEP 1- INSPECTION</h2>
      <ul class="side-list">
        <li><span class="term">Specialist-</span> a Harborline wildlife specialist inspects your attic and home exterior</li>
        <li><span class="term">Report-</span> a detailed report with pictures of any infestations found</li>
        <li><span class="term">Contamination-</span> any areas found to be contaminated are documented</li>
        <li><span class="term">Entry Points-</span> we identify current or potential entry points into the home</li>
      </ul>
    </div>

    <div class="side-section">
      <svg class="side-icon" width="64" height="48" viewBox="0 0 64 48" aria-hidden="true">
        <path d="M2 24 C16 2 48 2 62 24 C48 46 16 46 2 24 Z" fill="var(--icon-grey)"/>
        <circle cx="32" cy="24" r="14" fill="var(--light-bg)"/>
        <circle cx="32" cy="24" r="9" fill="var(--icon-grey)"/>
      </svg>
      <h2 class="side-heading">WHAT WE LOOK FOR</h2>
      <ul class="side-list">
        <li>Droppings, gnaw marks, runways, tracks and nesting in the attic, walls and around the structure</li>
      </ul>
    </div>
  </section>

  <section class="panel">
    <svg class="badge-award" width="90" height="90" viewBox="0 0 90 90" role="img" aria-label="Service award badge">
      <circle cx="45" cy="45" r="42" fill="var(--accent-gold)"/>
    </svg>

    <div class="badge-offer">
      <div class="buy">BUY NOW</div>
      <svg width="44" height="32" viewBox="0 0 44 32" aria-hidden="true">
        <path d="M2 4 H9 L14 22 H36 L40 9 H11" fill="none" stroke="#fff" stroke-width="3" stroke-linejoin="round"/>
        <circle cx="16" cy="28" r="3" fill="#fff"/><circle cx="33" cy="28" r="3" fill="#fff"/>
      </svg>
      <div class="deal">50% OFF<br>WHEN YOU<br>BUY &amp; SCHEDULE<br>ONLINE!</div>
    </div>

    <div class="col col-mid">
      <div class="mid-block">
        <h3 class="block-heading">
          <svg width="40" height="36" viewBox="0 0 40 36" aria-hidden="true"><g fill="#fff"><rect x="17" y="2" width="8" height="18" rx="1" transform="rotate(20 21 11)"/><path d="M4 32 H36 V36 H4 Z"/><rect x="22" y="24" width="10" height="6"/></g><path d="M10 31 C10 20 20 18 26 22" fill="none" stroke="#fff" stroke-width="4"/></svg>
          STEP 2- TRAPPING/REMOVAL
        </h3>
        <ul class="panel-list">
          <li>We create a plan to trap any infestation and remove the animals</li>
          <li>Each situation is different and may require a variety of techniques</li>
          <li>Traps are checked and animals removed on a set schedule</li>
        </ul>
      </div>
      <div class="mid-block">
        <h3 class="block-heading">
          <svg width="40" height="22" viewBox="0 0 40 22" aria-hidden="true"><path d="M20 11 C14 3 4 3 4 11 C4 19 14 19 20 11 C26 3 36 3 36 11 C36 19 26 19 20 11 Z" fill="none" stroke="#fff" stroke-width="5"/></svg>
          STEP 3- DECONTAMINATION
        </h3>
        <ul class="panel-list">
          <li>Animals leave behind urine, feces and oils</li>
          <li>These can contain a variety of bacteria and diseases</li>
          <li>Your treatment plan includes a process to remove and clean up these areas</li>
        </ul>
      </div>
      <div>
        <h3 class="block-heading">
          <svg width="36" height="44" viewBox="0 0 36 44" aria-hidden="true"><g fill="#fff"><rect x="10" y="8" width="7" height="22" rx="3.5"/><path d="M10 24 H30 C33 24 34 28 34 32 C34 40 28 44 20 44 C12 44 6 38 4 30 L10 26 Z"/></g><circle cx="13.5" cy="8" r="6" fill="none" stroke="#fff" stroke-width="2"/></svg>
          STEP 4- ENTRY PREVENTION
        </h3>
        <ul class="panel-list">
          <li>Once the infestation is eliminated we seal up any potential entry points</li>
          <li class="sub">• AC lines, window frames, garage door, roof piping and vents</li>
          <li class="sub">• Metal flashing and wire mesh where needed</li>
          <li>Sealing helps prevent any future infestations into the structure</li>
        </ul>
      </div>
    </div>

    <div class="col col-right">
      <h3 class="block-heading">
        <svg width="30" height="34" viewBox="0 0 30 34" aria-hidden="true"><path d="M15 2 L28 7 V16 C28 25 22 30 15 33 C8 30 2 25 2 16 V7 Z" fill="#fff"/></svg>
        STEP 5- ONGOING PROTECTION
      </h3>
      <ul class="panel-list">
        <li><span class="term">Baiting Program-</span> Harborline sets up a rodent baiting program around your home</li>
        <li class="sub">• Reduces any surrounding rodent populations</li>
        <li class="sub">• Bait stations are always secured and tamper resistant</li>
        <li><span class="term">Service Visits-</span> stations are checked, refilled and cleaned on each visit</li>
        <li class="sub">• Number and location of stations noted for every follow up</li>
        <li><span class="term">Re-Inspection-</span> entry points are checked again to confirm seals are holding</li>
        <li><span class="term">Reporting-</span> you receive notes and pictures after each service</li>
        <li class="sub">• Any new activity is addressed right away</li>
        <li><span class="term">Peace of Mind-</span> ongoing protection keeps your home pest free all year</li>
      </ul>
    </div>
  </section>

  <div class="footer-band"></div>
  <div class="footer-base"></div>
  <div class="site-url">www.harborlinetpc.com</div>
  <div class="follow">
    <span>Follow Us :</span>
    <i class="social-slot"></i><i class="social-slot"></i><i class="social-slot"></i><i class="social-slot"></i><i class="social-slot"></i>
  </div>

  <div class="brand-box">
    <div class="brand-name"><span class="main">Harborline</span><span class="sub">TERMITE &amp; PEST CONTROL</span></div>
    <div class="brand-mark"></div>
  </div>

</div>
</body>
</html>
```